Business card design

I already have the logo design completed and am requiring business card design and layout utilising the logo. I require a front and back design.

We are an executive recruitment company so we are looking at full colour, high finish in a reasonably conservative structure.
Updates

Reason: will be provide ai template

Target Market(s)

Senior Management 35-60 age bracket

Industry/Entity Type

Business

Requirements
Must have
• Tobias Wrenfield
• Director
• 48 Morrow Pde, Paddington QLD 4064
• Ph: 07 3944 2618 Mob: 0468925317
• tobias@orvandaexecutive.com.au
• www.orvandaexecutive.com.au
Nice to have
• Ideally full colour,
Should not have
• cheap looking

```html
<!DOCTYPE html>
<html lang="en">
<head>
<meta charset="utf-8">
<title>Orvanda Executive – Business Card</title>
<link rel="stylesheet" href="https://fonts.googleapis.com/css2?family=Roboto:wght@300;400&display=swap">
<style>
  :root {
    --page: #ffffff;
    --card-light: #e6e7e9;
    --navy: #1f3a68;
    --navy-deep: #1c3764;
    --band-grey: #5d5f63;
    --text-grey: #555a61;
    --dark-1: #8a8b8e;
    --dark-2: #6b6c70;
    --dark-3: #555659;
    --light-text: #e4e5e7;
    --web-text: #c9cacc;
  }
  * { box-sizing: border-box; margin: 0; padding: 0; }
  html, body {
    width: 1200px; height: 1027px; overflow: hidden;
    background: var(--page);
  }
  .sheet { position: relative; width: 1200px; height: 1027px; }

  .card {
    position: absolute; top: 55px; width: 530px; height: 924px;
    overflow: hidden;
  }
  .card--front { left: 57px; background: var(--card-light); }
  .card--back { left: 628px; }

  .brand {
    position: absolute; left: 0; right: 0;
    display: flex; align-items: center; justify-content: center; gap: 14px;
    font-family: "Roboto", sans-serif; font-weight: 400;
    font-size: 30px; line-height: 1; letter-spacing: 0.5px;
  }
  .brand__square { width: 32px; height: 32px; flex: none; }

  .card--front .brand { top: 124px; color: var(--navy); }
  .card--front .brand__square { background: var(--navy); }

  .person {
    position: absolute; top: 400px; left: 0; right: 0; text-align: center;
    font-family: "Roboto", sans-serif; color: var(--navy);
  }
  .person__name { font-size: 28px; font-weight: 400; letter-spacing: 1.5px; text-transform: uppercase; }
  .person__title { font-size: 27px; font-weight: 400; margin-top: 6px; }

  .contact {
    position: absolute; top: 518px; left: 0; right: 0; text-align: center;
    font-family: "Roboto", sans-serif; font-weight: 300; font-size: 17px;
    color: var(--text-grey); line-height: 23px;
  }

  .office {
    position: absolute; top: 830px; left: 0; right: 0; text-align: center;
    font-family: "Roboto", sans-serif; font-weight: 300; font-size: 15.5px;
    color: var(--text-grey); line-height: 23px;
  }

  .base-band {
    position: absolute; left: 0; right: 0; bottom: 0; height: 30px;
    display: flex;
  }
  .base-band__accent { width: 157px; background: var(--navy-deep); }
  .base-band__rest { flex: 1; background: var(--band-grey); }

  .back-texture {
    position: absolute; inset: 0;
    background:
      radial-gradient(ellipse 90% 40% at 80% 78%, rgba(255,255,255,0.10), transparent 70%),
      linear-gradient(180deg, var(--dark-1) 0%, var(--dark-2) 55%, var(--dark-3) 100%);
  }
  .card--back .brand { top: 445px; color: var(--light-text); font-size: 34px; }
  .card--back .brand__square { background: var(--light-text); width: 36px; height: 36px; }

  .website {
    position: absolute; top: 866px; left: 0; right: 0; text-align: center;
    font-family: "Roboto", sans-serif; font-weight: 300; font-size: 17px;
    color: var(--web-text); letter-spacing: 0.5px;
  }
</style>
</head>
<body>
<main class="sheet">

  <section class="card card--front" aria-label="Card front">
    <div class="brand">
      <span class="brand__square"></span>
      <span class="brand__name">Orvanda Executive</span>
    </div>

    <div class="person">
      <p class="person__name">Tobias Wrenfield</p>
      <p class="person__title">Director</p>
    </div>

    <div class="contact">
      <p>M. +61 468925317</p>
      <p>E. tobias@orvandaexecutive.com.au</p>
    </div>

    <div class="office">
      <p>48 Morrow Pde, Paddington Qld 4064, Australia</p>
      <p>P. +61 739442618 | E. info@orvandaexecutive.com.au</p>
    </div>

    <div class="base-band">
      <span class="base-band__accent"></span>
      <span class="base-band__rest"></span>
    </div>
  </section>

  <section class="card card--back" aria-label="Card back">
    <div class="back-texture" role="img" aria-label="Soft grey flowing wave texture"></div>
    <div class="brand">
      <span class="brand__square"></span>
      <span class="brand__name">Orvanda Executive</span>
    </div>
    <p class="website">www.orvandaexecutive.com.au</p>
  </section>

</main>
</body>
</html>
```